menu boards

we would like change our prices on our boards

oatmeal prices
small $3.00
Large $4.00

lunch specials
$8.95

breakfast specials
#1 $5.00
#2 $5.00
#3 $5.00
#4 $4.00
#5 $5.95
#6 $5.25
Please order by Number - No substitutions

```html
<!DOCTYPE html>
<html lang="en">
<head>
<meta charset="utf-8">
<title>Breakfast Specials</title>
<link rel="stylesheet" href="https://fonts.googleapis.com/css2?family=Montserrat:wght@900&family=Pacifico&family=Oswald:wght@500;600;700&family=Open+Sans:ital,wght@0,400;0,700;1,600&display=swap">
<style>
  :root {
    --bg-orange: #f7a04a;
    --brand-red: #e8202f;
    --ink: #111111;
    --white: #ffffff;
    --tag-orange: #f07a22;
    --tag-brown: #b4471e;
    --tag-light: #fbe9d8;
  }
  * { box-sizing: border-box; margin: 0; padding: 0; }
  html, body { width: 943px; height: 1200px; overflow: hidden; }
  body {
    background: var(--bg-orange);
    position: relative;
    font-family: "Open Sans", Arial, sans-serif;
  }
  .headline-main {
    position: absolute;
    left: 38px; top: 18px;
    font-family: "Montserrat", Arial, sans-serif;
    font-weight: 900;
    font-size: 100px;
    line-height: 1;
    color: var(--brand-red);
    white-space: nowrap;
    text-shadow: 3px 3px 0 var(--white), -3px -3px 0 var(--white), 3px -3px 0 var(--white), -3px 3px 0 var(--white), 0 3px 0 var(--white), 0 -3px 0 var(--white), 3px 0 0 var(--white), -3px 0 0 var(--white);
  }
  .headline-script {
    position: absolute;
    left: 222px; top: 38px;
    font-family: "Pacifico", cursive;
    font-size: 150px;
    line-height: 1.3;
    white-space: nowrap;
    color: var(--white);
    transform: rotate(-5deg);
    transform-origin: left center;
    -webkit-text-stroke: 10px var(--ink);
    paint-order: stroke fill;
    text-shadow: 5px 5px 0 var(--ink);
    z-index: 2;
  }
  .menu-grid { position: absolute; inset: 0; z-index: 1; }
  .special-card {
    position: absolute;
    width: 430px;
    background: var(--white);
    border: 2px solid var(--ink);
    overflow: hidden;
  }
  .col-left { left: 30px; }
  .col-right { left: 483px; }
  .row-1 { top: 298px; height: 290px; }
  .row-2 { top: 596px; height: 287px; }
  .row-3 { top: 890px; height: 290px; }
  .corner-flag {
    position: absolute; left: 0; top: 0;
    width: 160px; height: 135px;
  }
  .corner-number {
    position: absolute; left: 14px; top: 12px;
    font-family: "Oswald", Arial, sans-serif;
    font-weight: 500;
    font-size: 58px;
    line-height: 1;
    color: var(--white);
  }
  .dish-photo {
    position: absolute;
    left: 110px; top: 12px;
    width: 310px; height: 180px;
    border-radius: 40px;
    background: radial-gradient(ellipse at 35% 55%, #e2b37a 0%, #f3e6d6 55%, #ffffff 85%);
  }
  .dish-description {
    position: absolute;
    right: 156px; bottom: 16px;
    text-align: right;
    font-size: 18px;
    line-height: 23px;
    color: var(--ink);
    font-weight: 700;
    white-space: nowrap;
  }
  .dish-description .or { font-weight: 400; }
  .dish-description .coffee { font-style: italic; font-weight: 600; }
  .price-tag {
    position: absolute;
    left: 290px; bottom: 1px;
    width: 136px; height: 92px;
    display: flex; flex-direction: column;
    text-align: center;
    overflow: hidden;
  }
  .tag-number {
    flex: 0 0 20px;
    background: var(--tag-orange);
    border-radius: 14px 0 0 0;
    color: var(--white);
    font-family: "Oswald", Arial, sans-serif;
    font-weight: 600;
    font-size: 14px;
    line-height: 20px;
  }
  .tag-price {
    flex: 0 0 42px;
    background: var(--white);
    border-left: 2px solid var(--tag-orange);
    color: var(--brand-red);
    font-family: "Oswald", Arial, sans-serif;
    font-weight: 700;
    font-style: italic;
    font-size: 27px;
    line-height: 42px;
    overflow: hidden;
    text-shadow: 2px 1px 0 var(--ink);
  }
  .tag-price sup { font-size: 12px; line-height: 0; vertical-align: 12px; text-shadow: none; margin-right: 3px; }
  .tag-rule {
    flex: 0 0 15px;
    font-size: 10px;
    line-height: 15px;
    font-family: Arial, sans-serif;
    white-space: nowrap;
  }
  .tag-rule b { font-weight: 700; }
  .rule-subs { background: var(--tag-brown); color: var(--tag-light); }
  .rule-order { background: var(--tag-orange); color: var(--tag-light); }
</style>
</head>
<body>
  <h1 class="headline-main">BREAKFAST</h1>
  <div class="headline-script">Specials</div>

  <main class="menu-grid">
    <section class="special-card col-left row-1">
      <div class="dish-photo" role="img" aria-label="Egg, bacon and cheese roll on a plate with a small cup of coffee"></div>
      <svg class="corner-flag" viewBox="0 0 160 135" aria-hidden="true"><polygon points="0,0 160,0 0,135" fill="var(--brand-red)"/></svg>
      <span class="corner-number">1</span>
      <p class="dish-description">One Egg, Bacon, Ham<br><span class="or">or</span> Sausage on a Roll<br><span class="coffee">And Sm. Cup of Coffee</span></p>
      <div class="price-tag"><div class="tag-number">#1</div><div class="tag-price"><sup>$</sup>5.00</div><div class="tag-rule rule-subs"><b>No</b> Substitutions</div><div class="tag-rule rule-order">Please <b>Order By Number</b></div></div>
    </section>

    <section class="special-card col-right row-1">
      <div class="dish-photo" role="img" aria-label="Egg white and cheese English muffin with a small cup of coffee"></div>
      <svg class="corner-flag" viewBox="0 0 160 135" aria-hidden="true"><polygon points="0,0 160,0 0,135" fill="var(--brand-red)"/></svg>
      <span class="corner-number">2</span>
      <p class="dish-description">Egg Whites &amp; Cheese<br>on an English Muffin<br><span class="coffee">And Sm. Cup of Coffee</span></p>
      <div class="price-tag"><div class="tag-number">#2</div><div class="tag-price"><sup>$</sup>5.00</div><div class="tag-rule rule-subs"><b>No</b> Substitutions</div><div class="tag-rule rule-order">Please <b>Order By Number</b></div></div>
    </section>

    <section class="special-card col-left row-2">
      <div class="dish-photo" role="img" aria-label="Two fried eggs with potatoes and toast and a small cup of coffee"></div>
      <svg class="corner-flag" viewBox="0 0 160 135" aria-hidden="true"><polygon points="0,0 160,0 0,135" fill="var(--brand-red)"/></svg>
      <span class="corner-number">3</span>
      <p class="dish-description">Two Eggs Any Style<br>with Potatoes &amp; Toast<br><span class="coffee">And Sm. Cup of Coffee</span></p>
      <div class="price-tag"><div class="tag-number">#3</div><div class="tag-price"><sup>$</sup>5.00</div><div class="tag-rule rule-subs"><b>No</b> Substitutions</div><div class="tag-rule rule-order">Please <b>Order By Number</b></div></div>
    </section>

    <section class="special-card col-right row-2">
      <div class="dish-photo" role="img" aria-label="Egg and spinach wrap cut in half with a small cup of coffee"></div>
      <svg class="corner-flag" viewBox="0 0 160 135" aria-hidden="true"><polygon points="0,0 160,0 0,135" fill="var(--brand-red)"/></svg>
      <span class="corner-number">4</span>
      <p class="dish-description">Two Eggs in<br>a Healthy Wrap<br><span class="coffee">And Sm. Cup of Coffee</span></p>
      <div class="price-tag"><div class="tag-number">#4</div><div class="tag-price"><sup>$</sup>4.00</div><div class="tag-rule rule-subs"><b>No</b> Substitutions</div><div class="tag-rule rule-order">Please <b>Order By Number</b></div></div>
    </section>

    <section class="special-card col-left row-3">
      <div class="dish-photo" role="img" aria-label="French toast slices with syrup and a small cup of coffee"></div>
      <svg class="corner-flag" viewBox="0 0 160 135" aria-hidden="true"><polygon points="0,0 160,0 0,135" fill="var(--brand-red)"/></svg>
      <span class="corner-number">5</span>
      <p class="dish-description">Buttermilk Pancakes<br><span class="or">or</span> Challah French Toast<br><span class="coffee">And Sm. Cup of Coffee</span></p>
      <div class="price-tag"><div class="tag-number">#5</div><div class="tag-price"><sup>$</sup>5.95</div><div class="tag-rule rule-subs"><b>No</b> Substitutions</div><div class="tag-rule rule-order">Please <b>Order By Number</b></div></div>
    </section>

    <section class="special-card col-right row-3">
      <div class="dish-photo" role="img" aria-label="Ham and cheese on a toasted bagel with a small cup of coffee"></div>
      <svg class="corner-flag" viewBox="0 0 160 135" aria-hidden="true"><polygon points="0,0 160,0 0,135" fill="var(--brand-red)"/></svg>
      <span class="corner-number">6</span>
      <p class="dish-description">Ham &amp; Cheese<br>on a Toasted Bagel<br><span class="coffee">And Sm. Cup of Coffee</span></p>
      <div class="price-tag"><div class="tag-number">#6</div><div class="tag-price"><sup>$</sup>5.25</div><div class="tag-rule rule-subs"><b>No</b> Substitutions</div><div class="tag-rule rule-order">Please <b>Order By Number</b></div></div>
    </section>
  </main>
</body>
</html>
```